Red Kettle Pictures BIz Card

This will be a biz card for our independent film company
RED KETTLE PICTURES

we have a logo and i need to figure out how to post it to you!

Here is the info we need on the card:

LOGO

dorianne pasko (lower case!)
dP@RedKettlePix.example
407-555-0148

Red Kettle Pictures, LLC
www.RedKettlePix.example

stories that matter (tagline)

Target Market(s)

adults in the entertainment industry in USA.
need something creative feeling, a bit funky, not to overt.
something eye catchy that people will be inclined to keep.

ask me any questions you have!

Industry/Entity Type

It Company

Requirements
Must have
• good looking! clean and easy to get the contact info. not too busy.
Nice to have
• love the cards where the design is "continued" on the back side.

perhaps the tag and logo on the back side?!?

open to ideas!
Should not have
• nothing "cartoonish"

```html
<!DOCTYPE html>
<html lang="en">
<head>
<meta charset="utf-8">
<title>Red Kettle Pictures – Business Card</title>
<link rel="stylesheet" href="https://fonts.googleapis.com/css2?family=Roboto:wght@300;400;700&display=swap">
<style>
  :root {
    --paper: #ffffff;
    --ink: #1c1c1c;
    --red: #e32428;
    --edge: #3a3a3a;
  }
  * { margin: 0; padding: 0; box-sizing: border-box; }
  html, body {
    width: 1200px;
    height: 900px;
    overflow: hidden;
    background: var(--paper);
    font-family: "Roboto", Arial, sans-serif;
    color: var(--ink);
  }
  .canvas {
    position: relative;
    width: 1200px;
    height: 900px;
  }
  .card {
    position: absolute;
    top: 34px;
    width: 520px;
    height: 830px;
    background: var(--paper);
    border: 2px solid var(--edge);
    overflow: hidden;
  }
  .card--front { left: 66px; }
  .card--back { left: 640px; }

  /* front */
  .hero-art {
    position: absolute;
    left: 24px;
    top: 50px;
    width: 440px;
    height: 740px;
    border-radius: 40px 120px 60px 40px;
    background: linear-gradient(160deg, #e83236 0%, var(--red) 60%, #d01d21 100%);
  }
  .tagline {
    position: absolute;
    left: 140px;
    top: 40px;
    height: 760px;
    writing-mode: vertical-rl;
    transform: rotate(180deg);
    font-weight: 300;
    font-size: 74px;
    line-height: 1;
    letter-spacing: 1px;
    color: var(--ink);
    white-space: nowrap;
    text-align: left;
  }
  .brand {
    position: absolute;
    right: 14px;
    top: 12px;
    writing-mode: vertical-rl;
    font-weight: 400;
    font-size: 26px;
    line-height: 1;
    color: var(--ink);
    white-space: nowrap;
    display: flex;
    align-items: center;
    gap: 8px;
  }
  .brand__dot {
    width: 14px;
    height: 14px;
    border-radius: 50%;
    background: var(--red);
  }

  /* back */
  .film-band {
    position: absolute;
    left: 0;
    top: 0;
    width: 104px;
    height: 100%;
    background: var(--red);
  }
  .contact {
    position: absolute;
    left: 114px;
    top: 272px;
    font-size: 30px;
    line-height: 50px;
    color: var(--ink);
  }
  .contact__name {
    font-weight: 700;
    font-size: 35px;
  }
  .contact__gap { height: 50px; }
</style>
</head>
<body>
<div class="canvas">

  <section class="card card--front">
    <div class="hero-art" role="img" aria-label="Large red high-heel shoe illustration"></div>
    <div class="tagline">stories that matter . . .</div>
    <div class="brand"><span>Red Kettle Pictures</span><span class="brand__dot"></span></div>
  </section>

  <section class="card card--back">
    <div class="film-band" role="img" aria-label="Red film strip running down the card edge"></div>
    <div class="contact">
      <div class="contact__name">dorianne pasko</div>
      <div>dP@RedKettlePix.example</div>
      <div>407-555-0148</div>
      <div class="contact__gap"></div>
      <div>Red Kettle Pictures, LLC</div>
      <div>www.RedKettlePix.example</div>
    </div>
  </section>

</div>
</body>
</html>
```